Krautmann TFR
Zielgruppe
Brauereien, Sekt und Weinhersteller, bzw. Getränkehersteller - Abfüller national und international
Aufgabenstellung
Aktuelles Briefpapier mit dem beigefügten neuen LOGO auf neuesten Stand bringen

```html
<!DOCTYPE html>
<html lang="de">
<head>
<meta charset="utf-8">
<title>Krautmann TFR – Briefpapier</title>
<link rel="stylesheet" href="https://fonts.googleapis.com/css2?family=Barlow:wght@400;600&display=swap">
<style>
  :root {
    --brand-blue: #1f6fb8;
    --brand-blue-light: #3b8fd6;
    --text-grey: #5a5a5a;
    --paper: #ffffff;
  }
  * { margin: 0; padding: 0; box-sizing: border-box; }
  html, body { width: 848px; height: 1200px; overflow: hidden; background: var(--paper); }
  .letterhead {
    position: relative;
    width: 848px; height: 1200px;
    font-family: "Barlow", Arial, sans-serif;
    color: var(--text-grey);
    overflow: hidden;
  }
  .brand-mark {
    position: absolute; top: 70px; left: 611px; width: 187px;
    display: flex; align-items: center; justify-content: center; gap: 10px;
  }
  .brand-mark .square { width: 20px; height: 20px; background: var(--brand-blue); }
  .brand-mark .name {
    font-size: 27px; font-weight: 600; color: var(--brand-blue); letter-spacing: 0.5px;
    white-space: nowrap;
  }
  .return-line {
    position: absolute; top: 177px; left: 82px;
    font-size: 8.5px; white-space: nowrap;
  }
  .return-line .company { color: var(--brand-blue); }
  .contact-arc { position: absolute; top: 222px; left: 600px; }
  .contact-block {
    position: absolute; top: 237px; left: 605px; width: 200px;
    text-align: center; font-size: 9px; line-height: 14px;
  }
  .contact-block .company { color: var(--brand-blue); font-weight: 600; }
  .fold-mark { position: absolute; left: 0; width: 18px; height: 1px; background: #9a9a9a; }
  .fold-mark.upper { top: 403px; }
  .fold-mark.lower { top: 585px; }
  .footer-arc { position: absolute; top: 0; left: 0; }
  .footer {
    position: absolute; top: 1097px; left: 0; width: 848px;
    font-size: 8.5px; line-height: 13px; text-align: center;
  }
  .footer-col { position: absolute; width: 220px; }
  .footer-col.bank-one { left: 112px; }
  .footer-col.bank-two { left: 340px; }
  .footer-col.register { left: 550px; }
  .footer-col .heading { color: var(--brand-blue); font-weight: 600; }
</style>
</head>
<body>
<main class="letterhead">

  <div class="brand-mark">
    <span class="square"></span>
    <span class="name">Krautmann TFR</span>
  </div>

  <p class="return-line"><span class="company">Krautmann TFR Technik GmbH</span>| Werkstraße 24 | D-74211 Lindenau</p>

  <svg class="contact-arc" width="210" height="20" viewBox="0 0 210 20" aria-hidden="true">
    <path d="M2,18 Q105,-8 208,18" fill="none" stroke="var(--brand-blue-light)" stroke-width="1.2"/>
  </svg>

  <address class="contact-block" style="font-style:normal">
    <div class="company">Krautmann TFR Technik GmbH</div>
    <div>Werkstraße 24 | D-74211 Lindenau</div>
    <div>Tel: +49 (0) 712-355 40-0</div>
    <div>Fax: +49 (0) 712-355 40-200</div>
    <div>Mail: info@krautmann-tfr.com</div>
    <div>Web: www.krautmann-tfr.com</div>
  </address>

  <span class="fold-mark upper"></span>
  <span class="fold-mark lower"></span>

  <svg class="footer-arc" width="848" height="1200" viewBox="0 0 848 1200" aria-hidden="true">
    <path d="M0,945 Q424,1200 848,925" fill="none" stroke="var(--brand-blue)" stroke-width="1.5"/>
  </svg>

  <footer class="footer">
    <div class="footer-col bank-one">
      <div class="heading">Sparkasse Lindenau</div>
      <div>KTO: 204 51937</div>
      <div>BLZ: 610 502 04</div>
      <div>IBAN: DE41 6105 0204 0020 4519 37</div>
      <div>BIC: LNDSDE61XXX</div>
    </div>
    <div class="footer-col bank-two">
      <div class="heading">Nordhafen Bank AG</div>
      <div>KTO: 0539470 100</div>
      <div>BLZ: 620 300 18</div>
      <div>IBAN: DE57 6203 0018 0539 4701 00</div>
      <div>BIC: NHBKDE62XXX</div>
    </div>
    <div class="footer-col register">
      <div class="heading">Registergericht:</div>
      <div>Amtsgericht Lindenau</div>
      <div>HRB 518 267</div>
      <div>USt-ID-Nr.: DE275119304</div>
      <div>Geschäftsführer: Jonas Krautmann</div>
    </div>
  </footer>

</main>
</body>
</html>
```